Letterhead and Envelope for Mental Health Business

I need letterhead and envelope designs that will match my business cards. I am attaching a *.pds file of my business card so it can be matched.

```html
<!DOCTYPE html>
<html lang="en">
<head>
<meta charset="utf-8">
<title>Hale Counseling – Letterhead</title>
<link rel="stylesheet" href="https://fonts.googleapis.com/css2?family=Arimo:ital,wght@0,400;0,700;1,400&family=Roboto+Condensed:wght@400;700&display=swap">
<style>
  :root {
    --paper: #ffffff;
    --ink: #111111;
    --accent-blue: #2d5f9e;
    --accent-green: #6f9a3c;
    --mark-grey: #c9c9c9;
    --wash: #f2f2f2;
  }
  * { margin: 0; padding: 0; box-sizing: border-box; }
  html, body { width: 927px; height: 1200px; overflow: hidden; background: var(--paper); }
  .letterhead {
    position: relative;
    width: 927px;
    height: 1200px;
    background: var(--paper);
    font-family: "Roboto Condensed", "Arial Narrow", sans-serif;
    color: var(--ink);
  }
  .landscape-wash {
    position: absolute;
    left: 413px;
    top: 30px;
    width: 514px;
    height: 392px;
    background: radial-gradient(ellipse at 55% 45%, var(--wash) 0%, rgba(242,242,242,0.6) 45%, rgba(255,255,255,0) 72%);
  }
  .brand {
    position: absolute;
    left: 24px;
    top: 26px;
    width: 210px;
    text-align: center;
  }
  .brand-mark {
    display: flex;
    align-items: center;
    justify-content: center;
    gap: 8px;
    height: 68px;
  }
  .brand-dot {
    width: 22px;
    height: 22px;
    border-radius: 50%;
    background: var(--mark-grey);
    flex: none;
  }
  .brand-name {
    font-family: "Arimo", Arial, sans-serif;
    font-weight: 400;
    font-size: 19px;
    line-height: 1;
    color: var(--ink);
    white-space: nowrap;
  }
  .brand-person {
    margin-top: 10px;
    font-family: "Arimo", Arial, sans-serif;
    font-size: 23px;
    letter-spacing: 2.5px;
    color: var(--accent-blue);
  }
  .brand-credentials {
    margin-top: 4px;
    font-family: "Arimo", Arial, sans-serif;
    font-style: italic;
    font-size: 11px;
    letter-spacing: 2.6px;
    color: var(--accent-green);
  }
  .sender {
    position: absolute;
    left: 240px;
    top: 34px;
  }
  .sender-name { font-weight: 700; font-size: 16px; line-height: 20px; }
  .sender-credentials { font-size: 16px; line-height: 20px; }
  .contact-list { list-style: none; margin-top: 12px; }
  .contact-item {
    display: flex;
    align-items: center;
    gap: 6px;
    font-size: 10.5px;
    font-weight: 700;
    line-height: 18.5px;
    letter-spacing: -0.1px;
    white-space: nowrap;
  }
  .contact-icon { width: 12px; height: 10px; flex: none; }
</style>
</head>
<body>
<main class="letterhead">
  <div class="landscape-wash" role="img" aria-label="Faint grey illustration of a winding path with trees"></div>

  <header class="brand">
    <div class="brand-mark">
      <span class="brand-dot"></span>
      <span class="brand-name">Hale Counseling</span>
    </div>
    <p class="brand-person">Daniel Hale</p>
    <p class="brand-credentials">LMHC, NCC, DCC</p>
  </header>

  <section class="sender">
    <p class="sender-name">Daniel Hale</p>
    <p class="sender-credentials">LMHC, NCC, DCC</p>
    <ul class="contact-list">
      <li class="contact-item">
        <svg class="contact-icon" viewBox="0 0 12 10" aria-hidden="true"><path d="M1 3 Q6 0 11 3 L10 4.5 L8 4 L8 3 Q6 2.3 4 3 L4 4 L2 4.5 Z" fill="#111"/><rect x="2.5" y="5" width="7" height="4.5" rx="0.6" fill="none" stroke="#111"/></svg>
        <span>555/014-0198</span>
      </li>
      <li class="contact-item">
        <svg class="contact-icon" viewBox="0 0 12 10" aria-hidden="true"><rect x="0.7" y="1" width="10.6" height="8" fill="none" stroke="#111" stroke-width="1.2"/><path d="M0.7 1 L6 5.5 L11.3 1" fill="none" stroke="#111" stroke-width="1.2"/></svg>
        <span>Elm Street 48 1020 RIVERTON, USA</span>
      </li>
      <li class="contact-item">
        <svg class="contact-icon" viewBox="0 0 12 10" aria-hidden="true"><rect x="0.7" y="2" width="10.6" height="7.3" fill="none" stroke="#111"/><path d="M0.7 2 L6 6 L11.3 2" fill="none" stroke="#111"/><circle cx="10" cy="2" r="1.6" fill="#111"/></svg>
        <span>danielh@halecounselingllc.com</span>
      </li>
      <li class="contact-item">
        <svg class="contact-icon" viewBox="0 0 12 10" aria-hidden="true"><path d="M1 6 L5 2 L11 2 L11 5 L7 9 Z" fill="none" stroke="#111" stroke-width="1.2"/><circle cx="9" cy="3.6" r="0.9" fill="#111"/></svg>
        <span>www.halecounselingllc.com</span>
      </li>
    </ul>
  </section>
</main>
</body>
</html>
```